Cover Design For eBook "Norla"

I need two e-book covers with the same look and feel:

first one:
title
THE NORLA CAMPAIGN
subtitle
IGNITE DIGITAL GIVING
author
MERIDAN DONATIONS (just include the logo I attach)

second eBook
title
THE NORLA SYSTEM
subtitle
5 STEPS TO IGNITE YOUR CHURCH'S DIGITAL GIVING
author
MERIDAN DONATIONS (just include the log I attach)

Industry/Entity Type

Digital

Colors
f04a50
f68e4e
faa54b
ffcf3e

Requirements
Must have
• the MERIDAN DONATIONS LOGO I attached at the bottom of the design.
• There needs to be some type of spark coming off of one of the letters in NORLA
Nice to have
• I'd love to have a horizontal and vertical layout

```html
<!DOCTYPE html>
<html lang="en">
<head>
<meta charset="utf-8">
<title>The Norla Campaign – Ignite Digital Giving</title>
<link href="https://fonts.googleapis.com/css2?family=Oswald:wght@500&family=Montserrat:wght@400;600;700&display=swap" rel="stylesheet">
<style>
  :root {
    --amber-light: #ffcf3e;
    --amber: #faa54b;
    --orange: #f68e4e;
    --coral: #f04a50;
    --band: rgba(255, 226, 120, 0.9);
    --band-text: #f0606a;
    --white: #ffffff;
    --glow: rgba(255, 246, 214, 0.9);
  }
  * { margin: 0; padding: 0; box-sizing: border-box; }
  html, body { width: 800px; height: 1200px; overflow: hidden; }
  body { font-family: "Montserrat", Arial, sans-serif; }

  .cover {
    position: relative;
    width: 800px;
    height: 1200px;
    overflow: hidden;
    background: radial-gradient(ellipse at 50% 45%, var(--amber-light) 0%, var(--amber) 55%, var(--orange) 100%);
  }

  .cover-pattern {
    position: absolute;
    inset: 0;
    background: radial-gradient(ellipse at 50% 50%, rgba(255, 214, 120, 0.35) 0%, rgba(246, 142, 78, 0.15) 100%);
  }

  .title-line {
    position: absolute;
    left: 0;
    width: 100%;
    text-align: center;
    color: var(--white);
    line-height: 1;
    text-shadow: 0 0 14px rgba(255, 240, 200, 0.6);
  }
  .title-the {
    top: 112px;
    font-weight: 700;
    font-size: 62px;
    letter-spacing: 4px;
  }
  .title-name {
    top: 160px;
    font-family: "Oswald", "Arial Narrow", sans-serif;
    font-weight: 500;
    font-size: 180px;
    letter-spacing: 2px;
    text-shadow: 0 0 24px rgba(255, 240, 200, 0.7);
  }
  .title-name-word {
    position: relative;
    display: inline-block;
  }
  .title-spark {
    position: absolute;
    top: -70px;
    right: -50px;
    width: 110px;
    height: 110px;
    border-radius: 50%;
    background: radial-gradient(circle, var(--white) 0%, var(--glow) 14%, rgba(255, 246, 214, 0) 70%);
  }
  .title-campaign {
    top: 356px;
    font-weight: 700;
    font-size: 62px;
    letter-spacing: 5px;
  }

  .subtitle-band {
    position: absolute;
    top: 470px;
    left: 0;
    width: 100%;
    height: 56px;
    background: var(--band);
    display: flex;
    align-items: center;
    justify-content: center;
  }
  .subtitle {
    color: var(--band-text);
    font-weight: 400;
    font-size: 31px;
    letter-spacing: 1px;
    line-height: 1;
  }

  .cross-emblem {
    position: absolute;
    top: 580px;
    left: 245px;
    width: 310px;
    height: 430px;
    border-radius: 50%;
    background: radial-gradient(ellipse, rgba(255, 250, 230, 0.75) 0%, rgba(255, 236, 170, 0.35) 45%, rgba(255, 220, 120, 0) 72%);
  }

  .publisher {
    position: absolute;
    left: 80px;
    top: 1066px;
    display: flex;
    align-items: center;
    gap: 20px;
  }
  .publisher-dot {
    width: 54px;
    height: 54px;
    border-radius: 50%;
    background: var(--coral);
  }
  .publisher-name {
    color: var(--white);
    font-weight: 700;
    font-size: 44px;
    letter-spacing: 1px;
    line-height: 1;
  }
</style>
</head>
<body>
  <main class="cover">
    <div class="cover-pattern" role="img" aria-label="Faint decorative swirl and paisley pattern across the orange background"></div>

    <header>
      <div class="title-line title-the">THE</div>
      <h1 class="title-line title-name"><span class="title-name-word">NORLA<span class="title-spark" role="img" aria-label="Glowing spark flying off the last letter"></span></span></h1>
      <div class="title-line title-campaign">CAMPAIGN</div>
    </header>

    <div class="subtitle-band">
      <p class="subtitle">IGNITE DIGITAL GIVING</p>
    </div>

    <div class="cross-emblem" role="img" aria-label="Glowing outlined ornate cross"></div>

    <footer class="publisher">
      <span class="publisher-dot"></span>
      <span class="publisher-name">MERIDAN DONATIONS</span>
    </footer>
  </main>
</body>
</html>
```